Cozy Sprouts Business Cards

I need a business card for my new Company called Cozy Sprouts. We create handmade baby moccasins, headbands, t-shirts and more. I want some that will appeal to parents, and to go with the colors of my logo that I have attached. feel free to be creative. I would like my logo placed somewhere on the card.

Industry/Entity Type

Retail

Contact Information for Business Card

Cozy Sprouts
24816 Maplecrest D #5172
Irvine Ca 92738
Rosalind Vantrey Ceo
Info@Cozy-Sprouts.com
www.Cozy-Sprouts.com
Phone 9495817320

Requirements
Nice to have
• Logo included

```html
<!DOCTYPE html>
<html lang="en">
<head>
<meta charset="utf-8">
<title>Cozy Sprouts Business Card</title>
<link rel="stylesheet" href="https://fonts.googleapis.com/css2?family=Open+Sans:wght@400;600&display=swap">
<style>
  :root {
    --backdrop: #ece9e4;
    --card: #ffffff;
    --band: #141414;
    --copper: #e8956a;
    --ink: #1c1c1c;
    --muted: #4a4a4a;
    --stitch: #8a8a8a;
  }
  html, body {
    margin: 0;
    width: 1200px;
    height: 1022px;
    overflow: hidden;
    background: var(--backdrop);
    font-family: "Open Sans", Arial, sans-serif;
  }
  .card {
    position: absolute;
    left: 120px;
    top: 237px;
    width: 960px;
    height: 548px;
    background: var(--card);
    border-radius: 14px;
    overflow: hidden;
    box-shadow: 0 10px 30px rgba(0,0,0,0.18);
  }
  .card-art { position: absolute; inset: 0; }
  .brand {
    position: absolute;
    left: 64px;
    top: 190px;
    display: flex;
    align-items: center;
    gap: 16px;
  }
  .brand-square {
    width: 34px;
    height: 34px;
    background: var(--copper);
    border-radius: 6px;
  }
  .brand-name {
    font-size: 44px;
    font-weight: 400;
    color: var(--muted);
    letter-spacing: 0.5px;
  }
  .address {
    position: absolute;
    left: 64px;
    top: 282px;
    font-size: 21px;
    line-height: 30px;
    color: var(--copper);
  }
  .contacts {
    position: absolute;
    left: 64px;
    top: 362px;
    margin: 0;
    padding: 0;
    list-style: none;
    font-size: 21px;
    line-height: 34px;
    color: var(--muted);
  }
  .contacts li { display: flex; align-items: center; gap: 12px; }
  .contacts svg { width: 20px; height: 20px; flex: none; }
  .holder {
    position: absolute;
    right: 40px;
    top: 50px;
    text-align: right;
  }
  .holder-name {
    font-size: 36px;
    font-weight: 600;
    color: var(--ink);
    margin: 0;
    line-height: 46px;
  }
  .holder-title {
    font-size: 20px;
    color: var(--copper);
    margin: 2px 0 0;
  }
  .band-mark-square {
    position: absolute;
    left: 626px;
    top: 358px;
    width: 68px;
    height: 68px;
    background: var(--copper);
    border-radius: 12px;
    box-shadow: 0 0 0 6px var(--card);
  }
  .band-mark-name {
    position: absolute;
    left: 712px;
    top: 430px;
    font-size: 16px;
    color: #ffffff;
    white-space: nowrap;
  }
</style>
</head>
<body>
  <div class="card">
    <svg class="card-art" width="960" height="548" viewBox="0 0 960 548" role="img" aria-label="Black diagonal band with a pattern of small brand marks">
      <polygon points="440,548 960,180 960,548" fill="var(--band)"/>
      <line x1="416" y1="548" x2="960" y2="163" stroke="var(--stitch)" stroke-width="1.5" stroke-dasharray="7 5"/>
      <line x1="940" y1="548" x2="960" y2="530" stroke="var(--copper)" stroke-width="0"/>
      <rect x="954" y="180" width="6" height="368" fill="var(--copper)"/>
    </svg>

    <div class="brand">
      <div class="brand-square"></div>
      <span class="brand-name">Cozy Sprouts</span>
    </div>

    <div class="address">
      Cozy Sprouts 24816 Maplecrest D<br>
      #5172 Irvine Ca 92738
    </div>

    <ul class="contacts">
      <li>
        <svg viewBox="0 0 20 20"><path d="M5 2 L8 2 L9 6 L7 8 Q9 12 12 13 L14 11 L18 12 L18 15 Q17 18 14 18 Q4 16 2 5 Q2 2 5 2 Z" fill="none" stroke="var(--copper)" stroke-width="1.6"/></svg>
        9495817320
      </li>
      <li>
        <svg viewBox="0 0 20 20"><circle cx="10" cy="10" r="8" fill="none" stroke="var(--copper)" stroke-width="1.6"/><ellipse cx="10" cy="10" rx="3.5" ry="8" fill="none" stroke="var(--copper)" stroke-width="1.4"/><line x1="2" y1="10" x2="18" y2="10" stroke="var(--copper)" stroke-width="1.4"/></svg>
        www.Cozy-Sprouts.com
      </li>
      <li>
        <svg viewBox="0 0 20 20"><rect x="2" y="4" width="16" height="12" rx="1.5" fill="none" stroke="var(--copper)" stroke-width="1.6"/><polyline points="2,5 10,11 18,5" fill="none" stroke="var(--copper)" stroke-width="1.6"/></svg>
        Info@Cozy-Sprouts.com
      </li>
    </ul>

    <div class="holder">
      <p class="holder-name">Rosalind Vantrey</p>
      <p class="holder-title">Ceo</p>
    </div>

    <div class="band-mark-square"></div>
    <span class="band-mark-name">Cozy Sprouts</span>
  </div>
</body>
</html>
```